CPA, Management and IT Consulting Redesign Existing Website

We currently have a website that is outdated (www.kelvorant.com). We need a good website developer that can redesign our website. To make this easier I have chosen a few websites that we like the layout or template. Use our exiting website content for this project. Our new logo is attached below. Based on who wins this we will upgrade to a coded website and a content management system (CMS) so we can make changes to the text ourselves in the future.

http://www.marbeckhollis.com/
http://www.quorvelmanagement.com/

Target Market(s)

Government Clients

Industry/Entity Type

Management Consulting

Number of Pages Required

5+ page

Font styles to use
Serif

Requirements
Must have
• Please the following website templates as a guide.
• http://www.marbeckhollis.com/
• http://www.quorvelmanagement.com/
Nice to have
Should not have

```html
<!DOCTYPE html>
<html lang="en">
<head>
<meta charset="utf-8">
<title>Halbrook Enterprises, LLC</title>
<link href="https://fonts.googleapis.com/css2?family=Roboto:wght@400;500;700&family=Open+Sans:wght@400;600;700&display=swap" rel="stylesheet">
<style>
:root{
  --orange:#f7993a;
  --orange-dark:#e8862a;
  --ink:#222;
  --text:#666;
  --muted:#888;
  --light:#f4f4f4;
  --dark:#1d1d1d;
  --footer:#2b2b2b;
  --white:#fff;
}
*{margin:0;padding:0;box-sizing:border-box}
html,body{width:1200px;height:2871px;overflow:hidden}
body{position:relative;background:var(--white);font-family:"Open Sans",Arial,sans-serif;color:var(--text)}
.abs{position:absolute}
h2.section-title{position:absolute;left:0;width:1200px;text-align:center;font-family:"Roboto",Arial,sans-serif;font-weight:700;font-size:25px;color:var(--orange);letter-spacing:.5px}
.section-sub{position:absolute;left:200px;width:800px;text-align:center;font-size:13.5px;line-height:24px;color:var(--muted)}

/* header */
.site-header{left:0;top:0;width:1200px;height:115px;background:var(--white)}
.brand{left:100px;top:26px;display:flex;align-items:center;gap:10px}
.brand-mark{width:44px;height:44px;background:var(--orange)}
.brand-name{font-family:"Roboto",Arial,sans-serif;font-weight:700;font-size:25px;line-height:25px;color:var(--ink)}
.brand-tag{font-size:6.5px;letter-spacing:.4px;color:var(--orange);margin-top:4px}
.top-contact{top:24px;display:flex;align-items:center;gap:10px;font-size:12px;color:var(--text)}
.top-contact .ring{width:28px;height:28px;border:1.5px solid var(--orange);border-radius:50%;display:flex;align-items:center;justify-content:center}
.main-nav{top:70px;left:548px;display:flex;font-family:"Roboto",Arial,sans-serif;font-size:12px;font-weight:500;color:var(--ink)}
.main-nav a{display:block;padding:8px 0 0;height:45px;text-decoration:none;color:inherit;margin-right:52px}
.main-nav a.active{color:var(--orange);border-bottom:3px solid var(--orange);padding-left:16px;padding-right:16px;margin-left:-16px;margin-right:36px}
.search-ico{left:1088px;top:76px}

/* hero */
.hero{left:0;top:115px;width:1200px;height:512px;background:linear-gradient(110deg,#5a4a3d 0%,#8c7866 30%,#b9aa97 55%,#6f5e50 80%,#3b2f27 100%)}
.hero-caption{left:643px;top:275px;width:458px}
.hero-caption h1{background:rgba(20,20,20,.82);padding:22px 28px;font-family:"Roboto",Arial,sans-serif;font-weight:700;font-size:37px;color:var(--white);height:94px}
.hero-caption p{background:rgba(20,20,20,.6);padding:18px 28px;font-size:15px;line-height:27px;color:#eee;height:92px}
.hero-arrows{left:1044px;top:543px;display:flex;gap:8px}
.hero-arrows span{width:24px;height:24px;border-radius:50%;background:#444;display:flex;align-items:center;justify-content:center}

/* welcome */
.welcome{left:0;top:627px;width:1200px;height:321px;background:var(--light);border-bottom:1px solid #e3e3e3}
.welcome p{position:absolute;left:130px;width:940px;text-align:center;font-size:12.5px;line-height:24px;color:var(--muted)}
.btn{position:absolute;background:var(--orange);color:var(--white);font-family:"Roboto",Arial,sans-serif;font-weight:700;font-size:12px;text-align:center;text-transform:uppercase}

/* services */
.services{left:0;top:948px;width:1200px;height:447px;background:var(--white)}
.service{position:absolute;top:144px;width:262px;text-align:center}
.service .circle{width:122px;height:122px;margin:0 auto;border-radius:50%;border:6px solid #f1f1f1;background:var(--white);display:flex;align-items:center;justify-content:center}
.service h3{margin-top:22px;font-family:"Roboto",Arial,sans-serif;font-weight:700;font-size:13.5px;color:var(--ink)}
.service p{margin:12px auto 0;width:210px;font-size:12.5px;line-height:22px;color:var(--muted)}
.service .more{display:block;margin-top:12px;font-size:10px;font-weight:700;color:var(--orange);text-decoration:underline}
.divider{position:absolute;top:288px;width:1px;height:135px;background:#e6e6e6}

/* about */
.about{left:0;top:1395px;width:1200px;height:517px;background:linear-gradient(180deg,#1a1a1a,#262523 60%,#1c1b1a)}
.about .section-sub{color:#ddd}
.about-text{left:100px;top:182px;width:505px;font-size:12.5px;line-height:25px;color:#e6e6e6}
.about-text p+p{margin-top:24px}
.about-more{left:100px;top:416px;font-family:"Roboto",Arial,sans-serif;font-weight:700;font-size:12px;color:var(--orange)}
.about-media{left:646px;top:162px;width:456px;height:300px;border:4px solid var(--white);background:linear-gradient(135deg,#dfe8ee,#a9c3d6 55%,#6f8ea6)}

/* industries */
.industries{left:0;top:1912px;width:1200px;height:426px;background:var(--white)}
.industry{position:absolute;top:150px;width:230px;text-align:center}
.industry .thumb{height:168px;border:4px solid #f3f3f3;box-shadow:0 3px 6px rgba(0,0,0,.15)}
.industry h3{margin-top:28px;font-family:"Roboto",Arial,sans-serif;font-weight:700;font-size:13px;color:var(--ink);text-transform:uppercase}
.industry a{display:block;margin-top:8px;font-size:11px;font-style:italic;color:var(--orange);text-decoration:underline}

/* support */
.support{left:0;top:2338px;width:1200px;height:253px;background:linear-gradient(180deg,var(--orange),var(--orange-dark))}
.support h2{position:absolute;top:40px;left:0;width:1200px;text-align:center;font-family:"Roboto",Arial,sans-serif;font-weight:700;font-size:19px;color:var(--white)}
.support p{position:absolute;top:70px;left:0;width:1200px;text-align:center;font-size:12.5px;color:#fde2c4}
.badge{position:absolute;top:110px;width:157px;height:84px;background:var(--white);display:flex;align-items:center;justify-content:center}
.badge span{width:56px;height:30px;background:#e4e8ee;border-radius:3px}
.badge span.round{width:50px;height:50px;border-radius:50%;background:#d8dde6}

/* footer */
.site-footer{left:0;top:2591px;width:1200px;height:280px;background:var(--footer);color:#ddd}
.site-footer h4{font-family:"Roboto",Arial,sans-serif;font-weight:700;font-size:14px;color:var(--white);text-transform:uppercase}
.foot-col{position:absolute;top:42px}
.foot-nav li{list-style:none;font-size:10.5px;font-weight:700;color:var(--white);margin-top:14px}
.foot-col p{font-size:12px;line-height:18px;color:#ddd}
.news-input{margin-top:14px;width:286px;height:38px;background:#3a3a3a;border:1px solid #4a4a4a;font-size:11px;color:#999;padding:11px 14px}
.news-btn{margin-top:14px;width:96px;height:32px;background:var(--orange);color:var(--white);font-size:11px;font-weight:700;text-align:center;line-height:32px}
.contact-row{display:flex;gap:14px;margin-top:16px;font-size:11.5px;line-height:18px}
.social-row{display:flex;align-items:center;gap:12px;margin-top:12px;font-size:12px}
.social-row i{width:20px;height:20px;background:#ddd;border-radius:3px;display:block}
.copyright{position:absolute;left:0;top:244px;width:1200px;border-top:1px solid #3a3a3a;padding-top:10px;text-align:center;font-size:11.5px;color:#ccc}
</style>
</head>
<body>

<header class="site-header abs">
  <div class="brand abs">
    <div class="brand-mark"></div>
    <div>
      <div class="brand-name">HALBROOK<br>ENTERPRISES, LLC</div>
      <div class="brand-tag">CONSULTANTS AND CERTIFIED PUBLIC ACCOUNTANTS</div>
    </div>
  </div>
  <div class="top-contact abs" style="left:725px">
    <span class="ring"><svg width="12" height="10" viewBox="0 0 12 10"><rect x=".5" y=".5" width="11" height="9" fill="none" stroke="#f7993a"/><path d="M.5 .5 6 5.5 11.5 .5" fill="none" stroke="#f7993a"/></svg></span>
    dana.halbrook@kelvorant.com
  </div>
  <div class="top-contact abs" style="left:940px">
    <span class="ring"><svg width="12" height="12" viewBox="0 0 12 12"><path d="M2 1h2.5l1 3L4 5.2a7 7 0 0 0 2.8 2.8L8 6.5l3 1V10a1 1 0 0 1-1 1A9 9 0 0 1 1 2a1 1 0 0 1 1-1z" fill="#f7993a"/></svg></span>
    Phone: (202) 555-0147
  </div>
  <nav class="main-nav abs">
    <a class="active">HOME</a><a>ABOUT US</a><a>SERVICES</a><a>INDUSTRIES</a><a>CONTACT US</a>
  </nav>
  <svg class="search-ico abs" width="13" height="13" viewBox="0 0 13 13"><circle cx="5.5" cy="5.5" r="4" fill="none" stroke="#f7993a" stroke-width="2"/><path d="M8.5 8.5 12 12" stroke="#f7993a" stroke-width="2"/></svg>
</header>

<section class="hero abs" role="img" aria-label="Photo of a professional working at a laptop on an office desk with documents and coffee">
  <div class="hero-caption abs">
    <h1>FINANCIAL &amp; AUDITING</h1>
    <p>Sed ut perspiciatis unde omnis iste natus error sit voluptat accusantium doloremque laudantium, totam rem...</p>
  </div>
  <div class="hero-arrows abs">
    <span><svg width="8" height="10"><path d="M6 1 2 5l4 4" fill="none" stroke="#fff" stroke-width="2"/></svg></span>
    <span><svg width="8" height="10"><path d="M2 1l4 4-4 4" fill="none" stroke="#fff" stroke-width="2"/></svg></span>
  </div>
</section>

<section class="welcome abs">
  <h2 class="section-title" style="top:42px">WELCOME</h2>
  <p style="top:76px">Halbrook Enterprises, LLC and Ashford &amp; Crane, LLC is a network of certified public accounting and management consulting firms with seasoned professionals and an excellent reputation for serving a diverse client base including federal agencies, state and local government, non-profit organizations, small and medium-sized business entities, professional associations and individuals...</p>
  <p style="top:152px">We are committed to professional excellence across all service areas including Audit and Assurance, Accounting, Tax, Management Consulting, and Information Technology....</p>
  <div class="btn" style="left:529px;top:228px;width:143px;height:46px;line-height:46px;font-size:11px">Read More Info</div>
</section>

<section class="services abs">
  <h2 class="section-title" style="top:34px">SERVICES AND SOLUTIONS</h2>
  <div class="section-sub" style="top:70px">Sed ut perspiciatis unde omnis iste natus error sit voluptatem accusantium doloremque laudantium, totam rem aperiam, eaque ipsa quae ab illo inventore veritatis et quasi architecto</div>

  <div class="service" style="left:74px">
    <div class="circle"><svg width="56" height="56" viewBox="0 0 56 56" fill="none" stroke="#f7993a" stroke-width="2.5"><rect x="10" y="8" width="30" height="40" rx="2"/><path d="M16 18h18M16 26h18M16 34h12"/><path d="M44 20 30 44l-2 6 5-3 14-24z"/></svg></div>
    <h3>ACCOUNTING, AUDIT AND TAX</h3>
    <p>We offer a full range of assurance services that translates numbers into meaningful information...</p>
    <span class="more">READ MORE</span>
  </div>
  <div class="divider" style="left:336px"></div>
  <div class="service" style="left:336px">
    <div class="circle"><svg width="56" height="56" viewBox="0 0 56 56" fill="none" stroke="#f7993a" stroke-width="2.5"><path d="M20 10h16l-5 9h-6z"/><path d="M25 19c-10 6-14 14-14 20 0 7 6 9 17 9s17-2 17-9c0-6-4-14-14-20"/><text x="22" y="42" font-size="16" font-family="Roboto,sans-serif" fill="#f7993a" stroke="none">$</text></svg></div>
    <h3>FINANCIAL MANAGEMENT</h3>
    <p>Our knowledge of financial management regulatory requirements and industry best practicesrunner...</p>
    <span class="more">READ MORE</span>
  </div>
  <div class="divider" style="left:600px"></div>
  <div class="service" style="left:598px">
    <div class="circle"><svg width="56" height="56" viewBox="0 0 56 56" fill="none" stroke="#f7993a" stroke-width="2.5"><rect x="14" y="6" width="26" height="44" rx="4"/><path d="M24 43h6"/><circle cx="36" cy="30" r="9" fill="#f7993a" stroke="#fff"/><path d="M36 27v8M36 24v1" stroke="#fff" stroke-width="2"/></svg></div>
    <h3>INFORMATION TECHNOLOGY</h3>
    <p>As entities become more mobile,technology-reliant and geographically dispersed, opportunities...</p>
    <span class="more">READ MORE</span>
  </div>
  <div class="divider" style="left:862px"></div>
  <div class="service" style="left:860px">
    <div class="circle"><svg width="56" height="56" viewBox="0 0 56 56" fill="none" stroke="#f7993a" stroke-width="2.5"><circle cx="34" cy="16" r="9"/><text x="30" y="21" font-size="13" font-family="Roboto,sans-serif" fill="#f7993a" stroke="none">$</text><path d="M6 36h8l8-3h12c2 0 2 4 0 4H24"/><path d="M14 46h18l14-10c2-2 0-5-3-3l-9 5"/><rect x="4" y="33" width="8" height="16"/></svg></div>
    <h3>GOVERNANCE RISK &amp; COMPLIANCE</h3>
    <p>Constantly changing regulations are a challenge for every entity. Noncompliance can result in lost...</p>
    <span class="more">READ MORE</span>
  </div>
</section>

<section class="about abs">
  <h2 class="section-title" style="top:50px">ABOUT US</h2>
  <div class="section-sub" style="top:84px;left:260px;width:680px;color:#e2e2e2">Halbrook Enterprises, LLC (doing business as Ashford and Crane) and Ashford &amp; Crane, LLC are both certified public accounting and management consulting firms</div>
  <div class="about-text abs">
    <p>Halbrook Enterprises, LLC (doing business as Ashford and Crane) and Ashford &amp; Crane, LLC are both certified public accounting and management consulting firms with seasoned professionals and an excellent reputation for serving a diverse client base including fed sized business entities, professional associations and...</p>
    <p>Our diverse knowledge, backgrounds and subject-matter expertise help a wide variety of technology goals. We are firmly committed to delivering solutions with the expertise you need to tackle your complex challenges. We deliver unparalleled experiences, impeccable customer service and integrity with every engagement to...</p>
  </div>
  <div class="about-more abs">READ MORE INFORMATION</div>
  <div class="about-media abs" role="img" aria-label="Photo of a hand holding a pen over printed financial charts and a tablet"></div>
</section>

<section class="industries abs">
  <h2 class="section-title" style="top:42px">INDUSTRIES</h2>
  <div class="section-sub" style="top:76px">Sed ut perspiciatis unde omnis iste natus error sit voluptatem accusantium doloremque laudantium, totam rem aperiam, eaque ipsa quae ab illo inventore veritatis et quasi architecto</div>
  <div class="industry" style="left:100px"><div class="thumb" role="img" aria-label="Photo of a domed government capitol building under blue sky" style="background:linear-gradient(180deg,#3f7fc4,#8fb7e0 55%,#e5e2da 70%,#6b7a4d)"></div><h3>Federal Government</h3><a>Click View More Information!</a></div>
  <div class="industry" style="left:357px"><div class="thumb" role="img" aria-label="Photo of a legislative chamber with rows of desks" style="background:linear-gradient(180deg,#8a7a62,#6d4b30 50%,#9a8064)"></div><h3>State and Local Government</h3><a>Click View More Information!</a></div>
  <div class="industry" style="left:613px"><div class="thumb" role="img" aria-label="Photo of business people presenting financial charts" style="background:linear-gradient(135deg,#f2f4f7,#d6dfe8 50%,#9fb0c4)"></div><h3>Financial Management</h3><a>Click View More Information!</a></div>
  <div class="industry" style="left:870px"><div class="thumb" role="img" aria-label="Photo of a group of volunteers joining hands outdoors" style="background:linear-gradient(180deg,#a7c97a,#d8a46e 55%,#6e8f4a)"></div><h3>Not-for-Profit</h3><a>Click View More Information!</a></div>
</section>

<section class="support abs">
  <h2>SUPPORT</h2>
  <p>Sed ut perspiciatis unde omnis iste natus error sit voluptatem accusantium doloremque laudantium, totam rem aperiam.</p>
  <div class="badge" style="left:100px"><span></span></div>
  <div class="badge" style="left:267px"><span></span></div>
  <div class="badge" style="left:435px"><span></span></div>
  <div class="badge" style="left:605px"><span></span></div>
  <div class="badge" style="left:774px"><span class="round"></span></div>
  <div class="badge" style="left:943px"><span class="round"></span></div>
</section>

<footer class="site-footer abs">
  <div class="foot-col" style="left:100px">
    <h4>Navigation</h4>
    <ul class="foot-nav"><li>HOME</li><li>ABOUT US</li><li>SERVICES</li><li>INDUSTRIES</li><li>CONTACT US</li></ul>
  </div>
  <div class="foot-col" style="left:298px">
    <h4>Newsletter Subscription</h4>
    <p style="margin-top:8px;width:300px">Register Your email address to get informaiton about us</p>
    <div class="news-input">Email Address</div>
    <div class="news-btn">SUBSCRIBE</div>
  </div>
  <div class="foot-col" style="left:700px">
    <h4>Contact Us</h4>
    <div class="contact-row"><svg width="10" height="14" viewBox="0 0 10 14"><path d="M5 0a5 5 0 0 1 5 5c0 4-5 9-5 9S0 9 0 5a5 5 0 0 1 5-5z" fill="#ddd"/><circle cx="5" cy="5" r="2" fill="#2b2b2b"/></svg><span>4410 Larkmoor Street NW, Suite 300<br>Washington, DC 20016</span></div>
    <div class="contact-row"><svg width="12" height="12" viewBox="0 0 12 12"><path d="M2 1h2.5l1 3L4 5.2a7 7 0 0 0 2.8 2.8L8 6.5l3 1V10a1 1 0 0 1-1 1A9 9 0 0 1 1 2a1 1 0 0 1 1-1z" fill="#ddd"/></svg><span>Phone: (202) 555-0147</span></div>
    <div class="contact-row"><svg width="12" height="10" viewBox="0 0 12 10"><rect width="12" height="10" fill="#ddd"/><path d="M0 0 6 5 12 0" fill="none" stroke="#2b2b2b"/></svg><span>Email: info@kelvorant.com</span></div>
  </div>
  <div class="foot-col" style="left:992px">
    <h4>Follow Us On</h4>
    <div class="social-row"><i></i>Friendline</div>
    <div class="social-row"><i></i>Chirpcast</div>
    <div class="social-row"><i></i>Circleplus</div>
    <div class="social-row"><i></i>Pinboardly</div>
  </div>
  <div class="copyright">Copyright © 2016, Halbrook enterprises. All Rights Reserved.</div>
</footer>

</body>
</html>
```